Word Template for KESTREL Polls

KESTREL Polls stands for 'Kinship Evaluation Study Tracking Regional Everyday Lives Polls'. It is a collaborative research effort to format and combine multiple sources of public opinion data from around the world into merged datasets. We need a Microsoft Word template design for our research reports, dataset codebooks, crowdsourced development guidelines, and other documents that will be produced as part of the research and development. The template should match the website design and logo, which are attached to this contest (these are the files from previous successful design contests).

The main purpose will be to write reports discussing research and analysis. There will be lots data visualizations (bar charts, scatter plots, pie charts, histograms, trend line charts etc.) as well as tables, diargams, and photos mixed in wit all the text. A second purpose will be to write guidebooks to describe processes and teach others how to manage data, find variables, and write code, which will include screenshots and Word are diagrams and figures.

There are some document uploaded as examples for the kinds of things for which we need the template (working papers, codebooks, pamphlets, etc)

Target Market(s)

academia, government, non-profits, postgraduates, researchers

Font styles to use
Serif

Colors

Designer to choose colors to be used in the design.

Requirements
Must have
• A4 size page template
• Cover page
• Must match website design and logo (see attached)
Nice to have
• Colors to match logo and website (see attached)

```html
<!DOCTYPE html>
<html lang="en">
<head>
<meta charset="utf-8">
<title>KESTREL Polls – Report Template</title>
<link rel="stylesheet" href="https://fonts.googleapis.com/css2?family=Montserrat:wght@600;800&family=Carlito:wght@400;700&display=swap">
<style>
  :root {
    --blue-dark: #1b6fba;
    --blue-light: #27a3dd;
    --ink: #1c1c1c;
    --page: #ffffff;
    --backdrop: #f2f3f5;
  }
  * { box-sizing: border-box; margin: 0; padding: 0; }
  html, body { width: 1200px; height: 1200px; overflow: hidden; }
  body { background: var(--backdrop); position: relative; font-family: "Carlito", "Calibri", sans-serif; }

  .page {
    position: absolute; top: 233px; width: 567px; height: 734px;
    background: var(--page); overflow: hidden;
    box-shadow: 0 1px 3px rgba(0,0,0,0.08);
  }
  .page--cover { left: 17px; }
  .page--inner { left: 610px; }

  .brand {
    position: absolute; display: flex; align-items: center; gap: 8px;
    font-family: "Montserrat", sans-serif; font-weight: 600; color: var(--blue-dark);
    white-space: nowrap;
  }
  .brand__dot { border-radius: 50%; background: var(--blue-light); flex: none; }
  .page--cover .brand { left: 44px; top: 44px; font-size: 26px; }
  .page--cover .brand__dot { width: 30px; height: 30px; }
  .page--inner .brand { left: 26px; top: 30px; font-size: 18px; }
  .page--inner .brand__dot { width: 22px; height: 22px; }

  .photo { position: absolute; }
  .photo--cover {
    left: 6px; top: 110px; width: 556px; height: 330px;
    background: linear-gradient(135deg, #8a9b7a 0%, #c9b9a8 35%, #6b3f48 70%, #4a2a33 100%);
  }
  .photo--team {
    left: 7px; top: 154px; width: 557px; height: 239px;
    background: linear-gradient(90deg, #d9d6d2 0%, #c89868 30%, #e6ddd2 55%, #9a8a7e 80%, #d4d2d0 100%);
  }

  .cover-title {
    position: absolute; left: 56px; top: 463px;
    font-family: "Montserrat", sans-serif; font-weight: 800; font-size: 33px;
    color: var(--blue-dark); letter-spacing: 0.3px;
  }
  .cover-subtitle {
    position: absolute; left: 57px; top: 503px;
    font-family: "Montserrat", sans-serif; font-weight: 600; font-size: 14px;
    color: var(--blue-light);
  }
  .cover-mark {
    position: absolute; left: 462px; top: 583px; width: 120px; height: 120px;
    border-radius: 50%; background: var(--blue-light);
  }

  .section-heading {
    position: absolute; left: 7px; top: 98px; display: flex; align-items: center; gap: 18px;
    font-family: "Montserrat", sans-serif; font-weight: 800; font-size: 20px; color: var(--blue-light);
  }

  .body-copy {
    position: absolute; left: 67px; top: 416px; width: 460px;
    font-size: 12px; line-height: 17.3px; color: var(--ink); text-align: justify;
  }
  .body-copy p + p { margin-top: 7px; }

  .page-footer {
    position: absolute; left: 0; top: 696px; width: 100%; height: 20px;
    font-size: 10.5px; color: var(--blue-dark);
  }
  .page-footer__copyright { position: absolute; left: 27px; top: 3px; }
  .page-footer__rule { position: absolute; left: 221px; top: 1px; }
  .page-footer__number { position: absolute; left: 430px; top: 0; font-size: 13px; color: var(--blue-light); }
  .page-footer__mark {
    position: absolute; left: 534px; top: -8px; width: 34px; height: 34px;
    border-radius: 50%; background: var(--blue-light);
  }
</style>
</head>
<body>

<section class="page page--cover">
  <div class="brand"><span class="brand__dot"></span>KESTREL Polls</div>
  <div class="photo photo--cover" role="img" aria-label="Photo of a group of friends huddled together, seen from below, smiling into the lens"></div>
  <h1 class="cover-title">TITLE GOES HERE</h1>
  <p class="cover-subtitle">Subtitle Goes Here</p>
  <div class="cover-mark"></div>
</section>

<section class="page page--inner">
  <div class="brand"><span class="brand__dot"></span>KESTREL Polls</div>

  <h2 class="section-heading">
    <svg width="42" height="20" viewBox="0 0 42 20" aria-hidden="true">
      <line x1="0" y1="10" x2="24" y2="10" stroke="#1b6fba" stroke-width="3"/>
      <circle cx="32" cy="10" r="7.5" fill="none" stroke="#1b6fba" stroke-width="3"/>
    </svg>
    About Us
  </h2>

  <div class="photo photo--team" role="img" aria-label="Photo of a diverse group of people of all ages standing together against a light wall"></div>

  <div class="body-copy">
    <p>Lorem ipsum dolor sit amet, consectetur adipiscing elit, sed do eiusmod tempor incididunt ut labore et dolore magna aliqua. Ut enim ad minim veniam, quis nostrud exercitation ullamco laboris nisi ut aliquip ex ea commodo consequat. Duis aute irure dolor in reprehenderit in voluptate velit esse cillum dolore eu fugiat nulla pariatur.</p>
    <p>Excepteur sint occaecat cupidatat non proident, sunt in culpa qui officia deserunt mollit anim id est laborum. Sed ut perspiciatis unde omnis iste natus error sit voluptatem accusantium doloremque laudantium, totam rem aperiam, eaque ipsa quae ab illo inventore veritatis et quasi architecto beatae vitae dicta sunt explicabo.</p>
    <p>Neque porro quisquam est, qui dolorem ipsum quia dolor sit amet, consectetur, adipisci velit, sed quia non numquam eius modi tempora incidunt ut labore et dolore magnam aliquam quaerat voluptatem. Ut enim ad minima veniam, quis nostrum exercitationem ullam corporis suscipit laboriosam, nisi ut aliquid ex ea commodi consequatur.</p>
  </div>

  <footer class="page-footer">
    <span class="page-footer__copyright">© 2018 – Copyright KESTREL Polls</span>
    <svg class="page-footer__rule" width="200" height="14" viewBox="0 0 200 14" aria-hidden="true">
      <line x1="0" y1="7" x2="188" y2="7" stroke="#1b6fba" stroke-width="2.5"/>
      <circle cx="194" cy="7" r="4.5" fill="#fff" stroke="#1b6fba" stroke-width="2"/>
    </svg>
    <span class="page-footer__number">Page - 3</span>
    <div class="page-footer__mark"></div>
  </footer>
</section>

</body>
</html>
```